Fenwick Business Card Design

Photography business needs a logo. I would like to see creative licence on options on 1 & 2 sided. I really like the concept of a fully / partially frosted design. I have already used SketchHarbor for my Logo, so I am looking for the same level of assistance with this project.

Industry/Entity Type

Business

Font styles to use
Serif
Script

Requirements
Must have
• Must Have:
• - These are my contact details
• Name: Paul K Fenwick
• Mobile: 5183402917
• email: lisamerrow@quillpost.com

```html
<!DOCTYPE html>
<html lang="en">
<head>
<meta charset="utf-8">
<title>Paul K Fenwick – Business Card</title>
<link rel="stylesheet" href="https://fonts.googleapis.com/css2?family=Lustria&display=swap">
<style>
  :root {
    --bg-start: #1788bd;
    --bg-mid: #247699;
    --bg-end: #3b5864;
    --text-light: #f1f1f1;
    --icon-disc: #17748f;
    --hanger-line: #dcdedf;
    --art-light: #8f9293;
    --art-dark: #2c2c2c;
  }
  html, body {
    margin: 0;
    padding: 0;
    overflow: hidden;
    background: #ffffff;
  }
  .card {
    position: relative;
    width: 1200px;
    height: 540px;
    overflow: hidden;
    background: linear-gradient(115deg, var(--bg-start) 0%, var(--bg-mid) 45%, var(--bg-end) 100%);
    font-family: "Lustria", Georgia, serif;
    color: var(--text-light);
  }
  .card-art {
    position: absolute;
    inset: 0;
  }
  .holder-name {
    position: absolute;
    left: 272px;
    top: 205px;
    margin: 0;
    font-size: 124px;
    font-weight: 400;
    line-height: 1;
    letter-spacing: 1px;
    white-space: nowrap;
  }
  .contact-line {
    position: absolute;
    margin: 0;
    font-size: 32px;
    line-height: 1;
    white-space: nowrap;
  }
  .contact-phone { left: 100px; top: 433px; font-size: 34px; }
  .contact-email { left: 62px; top: 497px; }
</style>
</head>
<body>
<div class="card">
  <svg class="card-art" width="1200" height="540" viewBox="0 0 1200 540" xmlns="http://www.w3.org/2000/svg">
    <defs>
      <linearGradient id="art-tones" x1="0" y1="0" x2="1" y2="1">
        <stop offset="0" stop-color="var(--art-dark)"/>
        <stop offset="1" stop-color="var(--art-light)"/>
      </linearGradient>
    </defs>

    <g class="hanger-lines" stroke="var(--hanger-line)" stroke-width="6">
      <line x1="20" y1="235" x2="20" y2="500"/>
      <line x1="70" y1="235" x2="70" y2="428"/>
    </g>

    <circle class="lens-artwork-placeholder" role="img" aria-label="Camera lens illustration"
            cx="10" cy="22" r="222" fill="url(#art-tones)"/>

    <g class="icon-phone">
      <circle cx="70" cy="449" r="21" fill="var(--icon-disc)"/>
      <path d="M63 438 c-3 2 -4 5 -2 10 c2 6 6 11 11 13 c3 1 5 0 7 -2 l-4 -4 c-1 1 -2 1 -3 1 c-3 -2 -5 -5 -6 -8 c0 -1 0 -2 1 -3 z"
            fill="var(--text-light)"/>
    </g>
    <g class="icon-email">
      <circle cx="32" cy="513" r="21" fill="var(--icon-disc)"/>
      <path d="M19 510 L44 501 L38 524 L31 517 L27 522 L27 514 Z" fill="var(--text-light)"/>
      <path d="M27 514 L44 501" stroke="var(--icon-disc)" stroke-width="1.5" fill="none"/>
    </g>
  </svg>

  <h1 class="holder-name">Paul K Fenwick</h1>
  <p class="contact-line contact-phone">5183402917</p>
  <p class="contact-line contact-email">lisamerrow@quillpost.com</p>
</div>
</body>
</html>
```